Bitcoin Casino User Interface

This is a responsive design for a new bitcoin casino called the brass lantern casino

The 4 games I need the Ui for are video poker, blackjack, roulette and dice

The designs should be ideal for mobile and have a bit of a retro feel

Good example is www.pixelroulettehallcom

Target Market(s)

Adults between the ages of 21-55 all over the world

Industry/Entity Type

Casino

Font styles to use
Serif

Colors
5dc4b5
ffffff

Requirements
Must have
• Must be responsive and look great on mobile
design must be functional
Should not have
• Any generic and standard elements

```html
<!DOCTYPE html>
<html lang="en">
<head>
<meta charset="utf-8">
<title>Brass Lantern – Video Poker</title>
<link href="https://fonts.googleapis.com/css2?family=Oswald:wght@400;500;600;700&family=Roboto+Condensed:wght@700&display=swap" rel="stylesheet">
<style>
:root{
  --yellow:#ffd41c;
  --yellow-dark:#e0a812;
  --orange-text:#c9472a;
  --bar:#1c3a35;
  --bar-line:#2c524b;
  --felt-top:#1f5c53;
  --felt-bottom:#3f8f7d;
  --panel:#1d3934;
  --btn:#1a302c;
  --white:#ffffff;
  --red:#d2232a;
  --black:#141414;
  --muted:#4d7a70;
}
*{margin:0;padding:0;box-sizing:border-box}
html,body{width:1200px;height:737px;overflow:hidden;background:#0f1f1c}
body{font-family:'Oswald',sans-serif;color:var(--white);position:relative}
.screen{position:absolute;inset:0;background:linear-gradient(160deg,var(--felt-top) 0%,#24665a 45%,var(--felt-bottom) 100%);overflow:hidden}
.screen::before{content:"";position:absolute;left:500px;top:-200px;width:1200px;height:600px;background:rgba(255,255,255,.04);transform:rotate(18deg)}
.topbar{position:absolute;left:0;top:0;width:1200px;height:42px;background:var(--bar);border-bottom:1px solid var(--bar-line);display:flex;align-items:center;font-size:14px;font-weight:500;letter-spacing:-.2px}
.tab{height:42px;display:flex;align-items:center;justify-content:center;border-right:1px solid var(--bar-line);text-transform:uppercase}
.tab.active{background:var(--yellow);color:#2a2a2a;width:130px;gap:10px}
.tab.active .dot{width:9px;height:9px;border-radius:50%;background:#3b4a3a}
.tab.bj{width:115px}.tab.rl{width:100px}.tab.dc{width:82px}
.brand{position:absolute;left:525px;top:0;height:42px;display:flex;align-items:center;color:var(--yellow);font-size:19px;font-weight:600;text-transform:uppercase;letter-spacing:-.3px}
.nav-item{position:absolute;top:0;height:42px;display:flex;align-items:center;gap:10px;text-transform:uppercase;font-size:14px}
.nav-item .ico{width:18px;height:18px;border-radius:50%;background:var(--muted)}
.account{left:793px}.help{left:940px}.credits-top{left:1050px}
.credits-top b{color:var(--yellow);font-weight:500}
.hold{position:absolute;top:102px;width:101px;height:36px;background:var(--yellow);border:2px solid var(--yellow-dark);box-shadow:0 0 0 2px #f6b81a;color:var(--orange-text);font-size:20px;font-weight:600;display:flex;align-items:center;justify-content:center}
.card{position:absolute;top:151px;width:166px;height:255px;background:var(--white);border-radius:5px;box-shadow:0 3px 6px rgba(0,0,0,.3);font-family:'Roboto Condensed',sans-serif}
.card .idx{position:absolute;left:7px;top:10px;font-size:24px;line-height:22px;text-align:center}
.card .idx.br{left:auto;right:7px;top:auto;bottom:10px;transform:rotate(180deg)}
.card .idx span{display:block;font-size:20px}
.red{color:var(--red)}.blk{color:var(--black)}
.pip{position:absolute;font-size:40px;line-height:40px;transform:translate(-50%,-50%)}
.pip.flip{transform:translate(-50%,-50%) rotate(180deg)}
.face{position:absolute;left:28px;top:28px;width:110px;height:198px;border:1px solid #555}
.face.clubs{background:linear-gradient(180deg,#e9c23a 0%,#2b2b2b 45%,#c8322b 70%,#e9c23a 100%)}
.face.hearts{background:linear-gradient(180deg,#e9c23a 0%,#c8322b 40%,#2b2b2b 65%,#e9c23a 100%)}
.controls .btn{position:absolute;top:503px;height:45px;width:133px;background:var(--btn);border-radius:3px;display:flex;align-items:center;justify-content:center;font-size:15px;font-weight:500;box-shadow:0 2px 3px rgba(0,0,0,.3)}
.add{position:absolute;left:136px;top:510px;color:#f5a623;font-size:20px;font-weight:600;text-transform:uppercase}
.draw{position:absolute;left:482px;top:489px;width:232px;height:71px;background:var(--yellow);border:3px solid var(--orange-text);border-radius:6px;box-shadow:inset 0 0 0 3px #ffe56a;color:var(--orange-text);font-size:31px;font-weight:600;display:flex;align-items:center;justify-content:center}
.balance{position:absolute;left:915px;top:500px;color:#f5a623;font-weight:600;font-size:36px;text-transform:uppercase}
.balance small{font-size:22px}
.stakes{position:absolute;left:1037px;top:621px;width:127px;height:29px;background:var(--panel);color:#8fb8ae;font-size:12px;display:flex;align-items:center;justify-content:center;border-radius:3px 3px 0 0}
.paytable{position:absolute;left:0;top:650px;width:1200px;height:87px;background:var(--panel);border-top:1px solid var(--bar-line)}
.paytable .row{position:absolute;left:0;width:1200px;height:30px}
.paytable .row:first-child{top:12px}.paytable .row:last-child{top:42px;background:rgba(0,0,0,.12)}
.pay{position:absolute;top:0;height:30px;display:flex;align-items:center;font-size:13px;text-transform:uppercase}
.pay i{font-style:normal;color:var(--yellow);margin-left:auto}
.pay .dots{color:var(--yellow);letter-spacing:-1px;margin:0 4px}
</style>
</head>
<body>
<div class="screen">
  <header class="topbar">
    <div class="tab active"><span class="dot"></span>Poker</div>
    <div class="tab bj">Blackjack</div>
    <div class="tab rl">Roulette</div>
    <div class="tab dc">Dice</div>
    <div class="brand">Brass Lantern</div>
    <div class="nav-item account"><span class="ico"></span>My Account</div>
    <div class="nav-item help"><span class="ico"></span>Help</div>
    <div class="nav-item credits-top"><span class="ico"></span>Credits : <b>2873</b></div>
  </header>

  <div class="hold" style="left:169px">HOLD</div>
  <div class="hold" style="left:742px">HOLD</div>
  <div class="hold" style="left:933px">HOLD</div>

  <div class="card red" style="left:137px">
    <div class="idx">A<span>♥</span></div>
    <div class="pip" style="left:83px;top:124px">♥</div>
    <div class="idx br">A<span>♥</span></div>
  </div>
  <div class="card blk" style="left:328px">
    <div class="idx">9<span>♠</span></div>
    <div class="pip" style="left:48px;top:48px">♠</div><div class="pip" style="left:118px;top:48px">♠</div>
    <div class="pip" style="left:48px;top:98px">♠</div><div class="pip" style="left:118px;top:98px">♠</div>
    <div class="pip" style="left:83px;top:125px">♠</div>
    <div class="pip flip" style="left:48px;top:150px">♠</div><div class="pip flip" style="left:118px;top:150px">♠</div>
    <div class="pip flip" style="left:48px;top:202px">♠</div><div class="pip flip" style="left:118px;top:202px">♠</div>
    <div class="idx br">9<span>♠</span></div>
  </div>
  <div class="card red" style="left:517px">
    <div class="idx">4<span>♥</span></div>
    <div class="pip" style="left:50px;top:48px">♥</div><div class="pip" style="left:118px;top:48px">♥</div>
    <div class="pip flip" style="left:50px;top:204px">♥</div><div class="pip flip" style="left:118px;top:204px">♥</div>
    <div class="idx br">4<span>♥</span></div>
  </div>
  <div class="card blk" style="left:709px">
    <div class="idx">Q<span>♣</span></div>
    <div class="face clubs" role="img" aria-label="Queen of clubs court figure artwork"></div>
    <div class="idx br">Q<span>♣</span></div>
  </div>
  <div class="card red" style="left:900px">
    <div class="idx">Q<span>♥</span></div>
    <div class="face hearts" role="img" aria-label="Queen of hearts court figure artwork"></div>
    <div class="idx br">Q<span>♥</span></div>
  </div>

  <div class="controls">
    <div class="add">Add Credits</div>
    <div class="btn" style="left:303px">BET ONE</div>
    <div class="draw">DRAW</div>
    <div class="btn" style="left:749px">BET MAX</div>
    <div class="balance">2873 <small>Credits</small></div>
  </div>

  <div class="stakes">CHANGE STAKES</div>
  <section class="paytable">
    <div class="row">
      <div class="pay" style="left:46px;width:170px">Jacks or Better<i><span class="dots">..........</span>1</i></div>
      <div class="pay" style="left:282px;width:145px">3 of a Kind<i><span class="dots">..........</span>3</i></div>
      <div class="pay" style="left:505px;width:106px">Flush<i><span class="dots">..........</span>6</i></div>
      <div class="pay" style="left:738px;width:150px">4 of a Kind<i><span class="dots">..........</span>25</i></div>
      <div class="pay" style="left:965px;width:171px">Royal Flush<i><span class="dots">..........</span>250</i></div>
    </div>
    <div class="row">
      <div class="pay" style="left:46px;width:170px">Two Pair<i><span class="dots">..........</span>2</i></div>
      <div class="pay" style="left:282px;width:145px">Straight<i><span class="dots">..........</span>4</i></div>
      <div class="pay" style="left:505px;width:149px">Full House<i><span class="dots">..........</span>9</i></div>
      <div class="pay" style="left:738px;width:182px">Straight Flush<i><span class="dots">..........</span>50</i></div>
    </div>
  </section>
</div>
</body>
</html>
```